Let Us Bloom speaking engagement

the flyer is about a speaking engagement for women's groups. Flyer should be simple, soft, engaging, clean and professional. I am a life coach and also a talk show host. the event I will be advertising is for groups of women. It will be given to church groups, female clubs and organizations. The name of my company is Mara's Lantern Life Coaching Institute.

Target Market(s)

professional women over thirty years old

Font styles to use
Script

Colors
ffffff
34a7d8
85cae6

Requirements
Must have
• use my photo and logo only
Should not have
• anything distracting

```html
<!DOCTYPE html>
<html lang="en">
<head>
<meta charset="utf-8">
<title>Let Us Bloom – A Heart to Heart Conversation</title>
<link rel="stylesheet" href="https://fonts.googleapis.com/css2?family=Great+Vibes&family=Montserrat:ital,wght@0,600;1,700&family=Roboto:wght@400;700&display=swap">
<style>
  :root {
    --pink-light: #fdeef4;
    --pink-mid: #f3c3d9;
    --pink-deep: #e59ac0;
    --magenta: #b53f7f;
    --magenta-dark: #8c1f5a;
    --ink: #3e3038;
    --ink-soft: #5a4a53;
    --white: #ffffff;
    --logo-blue: #34a7d8;
    --logo-ink: #2d6f8c;
  }
  html, body {
    margin: 0;
    padding: 0;
    overflow: hidden;
    background: var(--white);
  }
  .flyer {
    position: relative;
    width: 1200px;
    height: 927px;
    overflow: hidden;
    background: radial-gradient(ellipse at 62% 30%, var(--pink-light) 0%, var(--pink-mid) 55%, var(--pink-deep) 100%);
    font-family: "Montserrat", Arial, sans-serif;
  }
  .flyer__swooshes {
    position: absolute;
    inset: 0;
    width: 1200px;
    height: 927px;
  }
  .portrait {
    position: absolute;
    left: 20px;
    top: 190px;
    width: 440px;
    height: 737px;
    border-radius: 50% 50% 0 0 / 28% 28% 0 0;
    background: linear-gradient(170deg, #2a2226 0%, #5b3b3c 32%, #9c6a5a 55%, #6e4a45 78%, #2c2228 100%);
  }
  .logo {
    position: absolute;
    left: 860px;
    top: 20px;
    width: 317px;
    height: 173px;
    background: var(--white);
    display: flex;
    align-items: center;
    justify-content: center;
    gap: 14px;
    padding: 0 20px;
    box-sizing: border-box;
  }
  .logo__dot {
    flex: none;
    width: 22px;
    height: 22px;
    border-radius: 50%;
    background: var(--logo-blue);
  }
  .logo__name {
    margin: 0;
    font-family: "Montserrat", Arial, sans-serif;
    font-weight: 600;
    font-size: 21px;
    line-height: 1.25;
    color: var(--logo-ink);
  }
  .intro {
    position: absolute;
    left: 80px;
    top: 100px;
    margin: 0;
    font-family: "Great Vibes", cursive;
    font-weight: 400;
    font-size: 54px;
    line-height: 1;
    color: var(--ink-soft);
    white-space: nowrap;
  }
  .coach-title {
    position: absolute;
    left: 455px;
    top: 238px;
    margin: 0;
    font-family: "Great Vibes", cursive;
    font-weight: 400;
    font-size: 80px;
    line-height: 1;
    color: var(--magenta-dark);
    white-space: nowrap;
  }
  .coach-name {
    position: absolute;
    left: 470px;
    top: 332px;
    margin: 0;
    font-family: "Great Vibes", cursive;
    font-weight: 400;
    font-size: 118px;
    line-height: 1;
    color: var(--magenta-dark);
    white-space: nowrap;
  }
  .session-blurb {
    position: absolute;
    left: 530px;
    top: 532px;
    width: 640px;
    margin: 0;
    font-family: "Montserrat", Arial, sans-serif;
    font-style: italic;
    font-weight: 700;
    font-size: 19px;
    line-height: 30px;
    text-align: center;
    color: var(--ink);
  }
  .session-blurb__line { display: block; white-space: nowrap; }
  .contact {
    position: absolute;
    right: 22px;
    bottom: 8px;
    margin: 0;
    font-family: "Roboto", Arial, sans-serif;
    font-size: 17px;
    line-height: 1.3;
    text-align: right;
    color: var(--ink);
  }
  .contact__line { display: block; }
  .contact__numbers { font-weight: 700; font-size: 19px; }
</style>
</head>
<body>
  <main class="flyer">
    <svg class="flyer__swooshes" viewBox="0 0 1200 927" aria-hidden="true">
      <path d="M0,0 L330,0 C170,60 60,150 0,300 Z" fill="#c9578f" opacity="0.55"/>
      <path d="M0,0 L180,0 C90,60 30,130 0,200 Z" fill="#a8306e" opacity="0.55"/>
      <path d="M560,0 C760,60 980,40 1200,0 L1200,30 C980,80 760,90 560,0 Z" fill="#ffffff" opacity="0.35"/>
      <path d="M380,700 C650,720 930,790 1200,840 L1200,927 L380,927 Z" fill="#f6d3e3"/>
      <path d="M380,680 C660,700 940,770 1200,815 L1200,850 C940,810 660,740 380,725 Z" fill="#b3407e"/>
      <path d="M380,725 C660,740 940,810 1200,850 L1200,862 C940,825 660,760 380,745 Z" fill="#d987b0" opacity="0.7"/>
    </svg>

    <div class="portrait" role="img" aria-label="Portrait photo of the life coach smiling, wearing black earrings and a beaded necklace"></div>

    <div class="logo">
      <span class="logo__dot" aria-hidden="true"></span>
      <p class="logo__name">Mara's Lantern Life Coaching Institute</p>
    </div>

    <p class="intro">A heart to heart conversation with</p>
    <h2 class="coach-title">Life Coach</h2>
    <h1 class="coach-name">Selene Marlow</h1>

    <p class="session-blurb">
      <span class="session-blurb__line">Let Us Bloom is an interactive soul searching session</span>
      <span class="session-blurb__line">that will help women share their stories and be real</span>
      <span class="session-blurb__line">about the things that matter most.</span>
    </p>

    <p class="contact">
      <span class="contact__line">To invite Selene to your women's group or gathering.</span>
      <span class="contact__line contact__numbers">Contact us at 242-555-0187 or 555-0142</span>
    </p>
  </main>
</body>
</html>
```